Most captivating card ever!

Life Coach - Professional Adventurer - Entrepreneur
I need the worlds most amazing business card for my personal brand. This business card will mostly be used to give to prospective clients for life coaching and business coaching.
Be creative, be adventurous. It needs to stand out. Make people say.. I need this guy!
My background is as an entrepreneur and professional adventurer undertaking extreme expeditions. I am now moving into life coaching.
No specific design ideas, so you have full creativity. Show me your best.
Industry/Entity Type
Life Coaching
Contact Information for Business Card
Mark Dellow
meetmark.com.au
0458260913
Colors
Designer to choose colors to be used in the design.
Look and feel

```html
<!DOCTYPE html>
<html lang="en">
<head>
<meta charset="utf-8">
<title>Mark Dellow – Business Card</title>
<link href="https://fonts.googleapis.com/css2?family=Montserrat:wght@400;700&family=Lato:wght@400&display=swap" rel="stylesheet">
<style>
  :root {
    --stage: #141414;
    --card: #0c0c0c;
    --card-edge: #1c1c1c;
    --ink: #f4f4f4;
    --accent: #f07f1a;
  }
  html, body {
    margin: 0;
    width: 1200px;
    height: 900px;
    overflow: hidden;
    background: var(--stage);
  }
  .stage {
    position: relative;
    width: 1200px;
    height: 900px;
  }
  .card {
    position: absolute;
    top: 300px;
    width: 520px;
    height: 298px;
    background: var(--card);
    border: 1px solid var(--card-edge);
    box-shadow: 0 18px 40px rgba(0,0,0,.6);
    overflow: hidden;
  }
  .card--contact { left: 50px; }
  .card--front { left: 630px; }

  .brand {
    position: absolute;
    display: flex;
    align-items: center;
    gap: 16px;
  }
  .card--contact .brand { left: 60px; top: 100px; }
  .card--front .brand { left: 60px; top: 108px; }

  .brand__dot {
    width: 54px;
    height: 54px;
    border-radius: 50%;
    background: var(--accent);
    flex: none;
  }
  .brand__name {
    font-family: "Montserrat", sans-serif;
    font-weight: 700;
    font-size: 34px;
    letter-spacing: 0.5px;
    color: var(--ink);
    text-transform: uppercase;
    line-height: 1;
    margin: 0;
  }
  .tagline {
    font-family: "Montserrat", sans-serif;
    font-weight: 400;
    font-size: 12.5px;
    color: var(--accent);
    margin: 8px 0 0;
    white-space: nowrap;
  }
  .contact-list {
    display: flex;
    gap: 18px;
    margin: 10px 0 0;
    padding: 0;
    list-style: none;
    font-family: "Lato", sans-serif;
    font-size: 17px;
    color: var(--ink);
    letter-spacing: 0.5px;
    white-space: nowrap;
  }
  .contact-list li {
    display: flex;
    align-items: center;
    gap: 6px;
  }
  .contact-list svg { width: 14px; height: 14px; fill: var(--accent); }
</style>
</head>
<body>
<main class="stage">

  <section class="card card--contact">
    <div class="brand">
      <span class="brand__dot" aria-hidden="true"></span>
      <div>
        <h1 class="brand__name">Mark Dellow</h1>
        <ul class="contact-list">
          <li>
            <svg viewBox="0 0 16 16" aria-hidden="true"><circle cx="8" cy="8" r="7" fill="none" stroke="#f07f1a" stroke-width="2"/><path d="M1 8h14M8 1c-3 4-3 10 0 14M8 1c3 4 3 10 0 14" fill="none" stroke="#f07f1a" stroke-width="1.4"/></svg>
            MEETMARK.COM.AU
          </li>
          <li>
            <svg viewBox="0 0 16 16" aria-hidden="true"><path d="M3 1h3l1.5 4-2 1.3a9 9 0 0 0 4.2 4.2L11 8.5l4 1.5v3a2 2 0 0 1-2 2A12 12 0 0 1 1 3a2 2 0 0 1 2-2z"/></svg>
            0458260913
          </li>
        </ul>
      </div>
    </div>
  </section>

  <section class="card card--front">
    <div class="brand">
      <span class="brand__dot" aria-hidden="true"></span>
      <div>
        <h2 class="brand__name">Mark Dellow</h2>
        <p class="tagline">Life Coach - Professional Adventurer - Entrepreneur</p>
      </div>
    </div>
  </section>

</main>
</body>
</html>
```